concept design for a website homepage

Hi, we are looking for a design for Homepage for our childcare centre
We want something really progressive, edgy, modern and premium. We want this website to standout but not cluttered. We only need a Homepage concept design for the below measurements.
1366 Wx768 H
The call to action is join our community
We like the idea of a split screen
Divided into 4 sections screen with the below
Locations and Enrolments
Tandel
Careers
Partnerships
We like angles and shapes, particularly triangles in the designs in the attached examples.
Our company font is Hands of Sean
Have attached some designs that we like the look and feel of and some of our designs from our flyers and some images to use, you don't need to choose all the images, just whatever works with your design.
We have a STEM focus at our centres so something sciency would be great.
Consider in the design will be viewed on desktop and mobile phones
1 page

```html
<!DOCTYPE html>
<html lang="en">
<head>
<meta charset="utf-8">
<title>Bright Spark Kindergarten – Menai</title>
<link href="https://fonts.googleapis.com/css2?family=Gochi+Hand&family=Montserrat:wght@400;500;600;700;800&display=swap" rel="stylesheet">
<style>
:root{
  --blue:#0aa4e3;
  --navy:#1b6fb5;
  --yellow:#ffec00;
  --green:#8cc63f;
  --green-dark:#6fa12a;
  --orange:#f7941d;
  --rust:#c63a12;
  --lime:#c8f51c;
  --royal:#3b7be8;
  --grey:#555759;
  --text:#6b6d70;
  --white:#ffffff;
}
*{margin:0;padding:0;box-sizing:border-box}
html,body{width:1200px;height:3566px;overflow:hidden}
body{position:relative;background:var(--white);font-family:'Montserrat',sans-serif;color:var(--text)}
.abs{position:absolute}
.hand{font-family:'Gochi Hand',cursive}

/* header */
.site-header{left:0;top:0;width:1200px;height:103px;background:var(--white);z-index:5}
.brand-box{left:48px;top:0;width:237px;height:241px;background:var(--blue);border-radius:0 0 14px 14px;z-index:6;display:flex;flex-direction:column;align-items:center;justify-content:center;gap:10px}
.brand-dot{width:62px;height:62px;border-radius:50%;background:var(--yellow)}
.brand-name{font-weight:800;color:var(--white);font-size:28px;line-height:1.05;text-align:center}
.main-nav{left:318px;top:40px;font-size:21px;color:var(--navy);white-space:nowrap}
.main-nav span{margin:0 6px}

/* hero */
.hero-photo{left:0;top:103px;width:1200px;height:800px;clip-path:polygon(0 0,100% 0,100% 100%,0 83.5%);
  background:
    linear-gradient(90deg,rgba(20,18,16,.55) 0%,rgba(20,18,16,.35) 50%,rgba(20,18,16,.05) 75%,rgba(20,18,16,.2) 100%),
    radial-gradient(ellipse 150px 110px at 860px 90px,#e0b81e 0%,rgba(224,184,30,.7) 45%,rgba(224,184,30,0) 100%),
    radial-gradient(ellipse 110px 90px at 790px 230px,#c9a88a 0%,rgba(201,168,138,0) 100%),
    radial-gradient(ellipse 290px 240px at 860px 420px,#1f5f8f 0%,#1a4a72 45%,rgba(26,74,114,0) 100%),
    radial-gradient(ellipse 110px 80px at 650px 580px,#c23b24 0%,rgba(194,59,36,0) 100%),
    radial-gradient(ellipse 110px 80px at 540px 640px,#b8a31a 0%,rgba(184,163,26,0) 100%),
    radial-gradient(ellipse 420px 180px at 400px 700px,#6e5232 0%,rgba(110,82,50,0) 100%),
    linear-gradient(180deg,#3a332c 0%,#4a4036 60%,#5a4630 100%)}
.hero-text{left:40px;top:310px;width:615px;text-align:center}
.hero-kicker{font-size:50px;color:var(--yellow);line-height:1}
.hero-title{font-weight:800;color:var(--white);font-size:84px;line-height:76px;margin-top:10px}
.hero-meta{font-size:31px;color:var(--green);margin-top:12px}
.join-btn{left:265px;top:606px;width:175px;height:56px;background:var(--blue);color:var(--white);border-radius:6px;font-size:30px;font-weight:500;display:flex;align-items:center;justify-content:center}

/* about */
.about-photo{left:75px;top:985px;width:408px;height:388px;
  background:
    radial-gradient(ellipse 190px 70px at 220px 350px,#d38a4a 0%,#c9a46a 40%,rgba(201,164,106,0) 100%),
    radial-gradient(ellipse 80px 130px at 120px 230px,#eef0f5 0%,rgba(238,240,245,0) 100%),
    radial-gradient(ellipse 70px 110px at 240px 220px,#eef0f5 0%,rgba(238,240,245,0) 100%),
    radial-gradient(ellipse 60px 110px at 395px 230px,#e8eaf0 0%,rgba(232,234,240,0) 100%),
    linear-gradient(180deg,#1b2340 0%,#2c3658 50%,#8a8aa0 100%)}
.about-kicker{left:527px;top:978px;font-size:25px;color:var(--blue)}
.about-title{left:527px;top:1012px;font-weight:700;font-size:48px;color:var(--grey)}
.about-copy{left:531px;top:1088px;width:582px;font-size:13px;line-height:22px}
.about-copy p+p{margin-top:22px}
.zigzag-deco{left:40px;top:1440px;width:155px;height:82px;border-radius:50%;background:radial-gradient(ellipse at center,rgba(247,148,29,.35) 0%,rgba(247,148,29,.12) 55%,rgba(247,148,29,0) 75%)}
.dots-deco{left:1044px;top:1380px;width:64px;height:64px;border-radius:50%;background:radial-gradient(circle,rgba(140,198,63,.45) 0%,rgba(140,198,63,.15) 55%,rgba(140,198,63,0) 72%)}

/* showcase */
.showcase-photo{left:0;top:1495px;width:1200px;height:748px;clip-path:polygon(0 12%,100% 0,100% 89.5%,0 100%);
  background:
    radial-gradient(ellipse 260px 120px at 600px 600px,#e07c2c 0%,rgba(224,124,44,0) 100%),
    radial-gradient(ellipse 120px 90px at 620px 330px,#2f5bb8 0%,rgba(47,91,184,0) 100%),
    radial-gradient(ellipse 220px 260px at 180px 420px,#c9641e 0%,rgba(201,100,30,0) 100%),
    radial-gradient(ellipse 260px 230px at 1040px 420px,#e8eef6 0%,#9fb0c8 45%,rgba(159,176,200,0) 100%),
    linear-gradient(180deg,#121832 0%,#1c2446 28%,#4a4e78 45%,#6a5a72 62%,#c8781e 85%,#e2a040 100%)}

/* tiles */
.feature-photo{left:54px;top:2360px;width:517px;height:504px;
  background:
    radial-gradient(ellipse 120px 170px at 150px 360px,#f4f0ea 0%,rgba(244,240,234,0) 100%),
    radial-gradient(ellipse 110px 160px at 390px 230px,#c46a3a 0%,rgba(196,106,58,0) 100%),
    radial-gradient(ellipse 140px 90px at 390px 400px,#3c5c8c 0%,rgba(60,92,140,0) 100%),
    radial-gradient(ellipse 130px 200px at 80px 120px,#b5583e 0%,rgba(181,88,62,0) 100%),
    linear-gradient(180deg,#e8e0d4 0%,#d8c8b4 60%,#b89272 100%)}
.tile{width:243px;height:241px;overflow:hidden}
.tile-photo{position:absolute;inset:0}
.tile-band{position:absolute;left:0;right:0;bottom:0;height:68px;clip-path:polygon(0 22%,60% 0,100% 14%,100% 100%,0 100%);display:flex;align-items:flex-end;justify-content:center;padding-bottom:10px;font-family:'Gochi Hand',cursive;font-size:28px;line-height:25px;text-align:center;color:var(--white)}
.tile-locations{left:597px;top:2360px}
.tile-tandel{left:866px;top:2360px}
.tile-careers{left:597px;top:2627px}
.tile-partners{left:866px;top:2627px}
.tile-locations .tile-band{justify-content:flex-start;padding-left:26px;text-align:left}

/* footer */
.footer-logo{left:481px;top:2998px;width:194px;height:205px;background:var(--blue);border-radius:10px;display:flex;flex-direction:column;align-items:center;justify-content:center;gap:10px;z-index:3}
.footer-logo .brand-dot{width:52px;height:52px}
.footer-logo .brand-name{font-size:23px}
.footer-info{left:0;top:3238px;width:1200px;text-align:center;color:var(--white);z-index:3}
.footer-office{font-weight:700;font-size:19px}
.footer-address{font-size:19px;margin-top:2px}
.footer-phone{font-size:38px;line-height:36px;margin-top:20px}
.footer-links{font-weight:600;font-size:19px;margin-top:26px}
.footer-social{display:flex;justify-content:center;gap:9px;margin-top:22px}
.footer-social span{width:32px;height:32px;border-radius:50%;background:var(--white)}
.copyright{left:0;top:3530px;width:1200px;height:36px;background:var(--blue);color:var(--white);font-weight:600;font-size:19px;display:flex;align-items:center;justify-content:center;z-index:3}
</style>
</head>
<body>

<header class="abs site-header">
  <nav class="abs main-nav hand">Homepage<span>|</span>About Us<span>|</span>Gallery<span>|</span>Spark Advantage™<span>|</span>Locations<span>|</span>Request a Tour<span>|</span>Join Waitlist</nav>
</header>
<div class="abs brand-box"><div class="brand-dot"></div><div class="brand-name">Bright Spark<br>Kindergarten</div></div>

<section>
  <div class="abs hero-photo" role="img" aria-label="Young child in hard hat and safety goggles using a toy drill at a workbench"></div>
  <svg class="abs" style="left:0;top:680px" width="1200" height="340" viewBox="0 680 1200 340">
    <polygon points="0,700 152,785 0,880" fill="#ffec00"/>
    <polygon points="1047,902 1200,815 1200,995" fill="#0aa4e3"/>
    <rect x="102" y="847" width="56" height="56" transform="rotate(-40 130 875)" fill="none" stroke="#8cc63f" stroke-width="4"/>
    <polygon points="1014,918 1074,953 1014,988" fill="none" stroke="#0aa4e3" stroke-width="4"/>
  </svg>
  <div class="abs hero-text">
    <div class="hero-kicker hand">join our</div>
    <h1 class="hero-title">MENAI<br>COMMUNITY</h1>
    <div class="hero-meta">6 weeks- 6 years | 7:00 am - 6:00 pm</div>
  </div>
  <div class="abs join-btn">JOIN</div>
</section>

<section>
  <div class="abs about-photo" role="img" aria-label="Children in lab coats looking at a model volcano in a sand table"></div>
  <div class="abs about-kicker hand">About us</div>
  <h2 class="abs about-title">Our school</h2>
  <div class="abs about-copy">
    <p>We are a warm, curious learning space where children explore science, art and play every day. Our educators guide each child through hands-on discovery, building confidence, kindness and a love of questions. Small groups, bright rooms and caring routines help every family feel at home from the very first visit. Menus are cooked fresh on site, and outdoor areas invite climbing, digging and gardening in all seasons.</p>
    <p>Our STEM program turns everyday moments into experiments, from building towers to watching seeds grow. Children test ideas, share results and celebrate mistakes as part of learning. Visit us to see how the day unfolds, meet the team and find the room that suits your child best.</p>
  </div>
  <div class="abs zigzag-deco" role="img" aria-label="Orange zigzag line decoration"></div>
  <div class="abs dots-deco" role="img" aria-label="Green dot cluster decoration"></div>
</section>

<section>
  <div class="abs showcase-photo" role="img" aria-label="Tandel imagination room with starry ceiling, dinosaur displays and colourful seating"></div>
  <svg class="abs" style="left:0;top:2150px" width="1200" height="120" viewBox="0 2150 1200 120">
    <polygon points="990,2184 1200,2166 1200,2242" fill="#f7941d"/>
    <rect x="60" y="2197" width="56" height="56" transform="rotate(-40 88 2225)" fill="none" stroke="#8cc63f" stroke-width="4"/>
  </svg>
</section>

<section>
  <div class="abs feature-photo" role="img" aria-label="Educator showing a child drawings of happy and sad faces"></div>
  <div class="abs tile tile-locations">
    <div class="tile-photo" role="img" aria-label="Educator and toddler playing with dough" style="background:radial-gradient(ellipse 70px 80px at 190px 130px,#e0409a 0%,rgba(224,64,154,0) 100%),radial-gradient(ellipse 90px 80px at 70px 110px,#244a86 0%,rgba(36,74,134,0) 100%),linear-gradient(180deg,#f2ede6 0%,#e6d8c6 60%,#c9b39a 100%)"></div>
    <div class="tile-band" style="background:var(--blue)">LOCATIONS &amp;<br>ENROLMENTS</div>
  </div>
  <div class="abs tile tile-tandel">
    <div class="tile-photo" role="img" aria-label="Educator showing a small object to a curious child" style="background:radial-gradient(ellipse 80px 90px at 190px 110px,#9fb8dc 0%,rgba(159,184,220,0) 100%),radial-gradient(ellipse 70px 80px at 60px 130px,#c98e6a 0%,rgba(201,142,106,0) 100%),linear-gradient(180deg,#f4f4f4 0%,#e6e8ec 100%)"></div>
    <div class="tile-band" style="background:var(--rust)">TANDEL</div>
  </div>
  <div class="abs tile tile-careers">
    <div class="tile-photo" role="img" aria-label="Child playing with colourful gear toys on a wall" style="background:radial-gradient(circle 40px at 60px 80px,#e0302a 0%,rgba(224,48,42,0) 100%),radial-gradient(circle 40px at 110px 110px,#2a7ad8 0%,rgba(42,122,216,0) 100%),radial-gradient(circle 35px at 70px 150px,#f2c200 0%,rgba(242,194,0,0) 100%),radial-gradient(ellipse 90px 120px at 200px 110px,#4a3a34 0%,rgba(74,58,52,0) 100%),linear-gradient(180deg,#ecebee 0%,#d8d2d0 100%)"></div>
    <div class="tile-band" style="background:var(--lime);color:#e0302a">CAREERS</div>
  </div>
  <div class="abs tile tile-partners">
    <div class="tile-photo" role="img" aria-label="Educator taking notes while a child plays" style="background:radial-gradient(ellipse 70px 90px at 70px 110px,#c98a6a 0%,rgba(201,138,106,0) 100%),radial-gradient(ellipse 50px 60px at 195px 150px,#a8c4de 0%,rgba(168,196,222,0) 100%),linear-gradient(180deg,#f6f6f6 0%,#e4e7ea 100%)"></div>
    <div class="tile-band" style="background:var(--royal)">PARTNERSHIPS</div>
  </div>
</section>

<footer>
  <svg class="abs" style="left:0;top:3020px" width="1200" height="546" viewBox="0 3020 1200 546">
    <path d="M0,3114 Q600,2950 1200,3114 L1200,3566 L0,3566 Z" fill="#8cc63f"/>
    <path d="M0,3114 Q600,2950 1200,3114" fill="none" stroke="#6fa12a" stroke-width="8"/>
    <polygon points="764,3140 830,3170 780,3215" fill="none" stroke="#a4d266" stroke-width="3"/>
    <polygon points="1048,3200 1108,3235 1048,3270" fill="none" stroke="#a4d266" stroke-width="3"/>
    <rect x="80" y="3290" width="56" height="56" transform="rotate(-40 108 3318)" fill="none" stroke="#a4d266" stroke-width="3"/>
    <polygon points="228,3395 295,3380 280,3445" fill="none" stroke="#a4d266" stroke-width="3"/>
  </svg>
  <div class="abs footer-logo"><div class="brand-dot"></div><div class="brand-name">Bright Spark<br>Kindergarten</div></div>
  <div class="abs footer-info">
    <div class="footer-office">Bright Spark Education™ – Head office</div>
    <div class="footer-address">Address - Suite 4, 88 Harbour Road, Westfield Park 2300</div>
    <div class="footer-phone hand">T: (02) 9000 1234 for NSW or<br>(07) 5000 6789 for QLD</div>
    <div class="footer-links">Sitemap &nbsp;|&nbsp; Privacy Policy &nbsp;|&nbsp; Contact</div>
    <div class="footer-social"><span></span><span></span><span></span><span></span></div>
  </div>
  <div class="abs copyright">© 2022 Bright Spark Kindergarten™</div>
</footer>

</body>
</html>
```